Mobile (Android/iPhone) game studio needs stationary design and a business card

We are Plunk Ferret Software and we need a fun and creative stationary design. Our company builds Android and iPhone games and children's software. The stationary designs should reflect an entertainment, fun and creativity. The pieces of stationary we need are:
1. A4 and Letter Word template (company letterhead)
2. A4 and Letter PPT template
3. Business card
4. Envelopes of various standard sizes
Each of the designs should somehow utilize our company logo.
The business card should have the following:
1. Incorporates our company logo (see attached)
2. Has a front and back with the same design (front is English, back is Traditional Chinese)
3. Delivered in an editable template so we can easily add new business cards using the same template when we hire more employees
4. Field for full name
5. Field for employee's title
6. Field for employee's email address
7. Field for company phone number - +886-2-51384470
8. Field for mobile phone number
9. Field for company fax number - +886-2-51384492
10. Company website address: www.plunkferret.example
11. Company address (on English side): 7F-2, NO. 63, Lane 91, Guoyuan Road, Dali District, Taipei Taiwan
12. Company address (on Traditional Chinese side): See Word document attachment for address in Chinese characters
Industry/Entity Type
Games
Look and feel
Each slider illustrates characteristics of the customer's brand and the style your logo design should communicate.

```html
<!DOCTYPE html>
<html lang="en">
<head>
<meta charset="utf-8">
<title>Plunk Ferret Software – Stationery</title>
<link href="https://fonts.googleapis.com/css2?family=Questrial&family=Noto+Sans+TC:wght@400&display=swap" rel="stylesheet">
<style>
  :root {
    --bg: #1d2023;
    --brand-blue: #1a56ad;
    --brand-blue-deep: #0c367f;
    --brand-navy: #1d1f86;
    --sky: #2f8fe0;
    --paper: #f4f5f7;
    --paper-shade: #e6e8ec;
    --swoosh-grey: #8a8d92;
    --ink: #55585e;
    --white: #ffffff;
  }
  * { box-sizing: border-box; margin: 0; padding: 0; }
  html, body { width: 1200px; height: 900px; overflow: hidden; }
  body {
    background: var(--bg);
    font-family: "Questrial", "Noto Sans TC", sans-serif;
    position: relative;
  }

  /* Letterhead */
  .letterhead {
    position: absolute; left: 70px; top: 70px;
    width: 540px; height: 764px;
    background: linear-gradient(160deg, var(--white), var(--paper-shade));
    overflow: hidden;
  }
  .letterhead__header { position: absolute; inset: 0 0 auto 0; height: 170px; }
  .letterhead__header svg { width: 100%; height: 100%; display: block; }
  .letterhead__brand {
    position: absolute; top: 58px; left: 0; right: 0;
    display: flex; justify-content: center;
  }
  .letterhead__footer {
    position: absolute; left: 0; right: 0; bottom: 46px;
    display: flex; align-items: center; justify-content: center; gap: 28px;
  }
  .footer-rule { flex: 1; height: 7px; background: var(--brand-navy); }
  .footer-rule--left { transform: skewY(-1deg); }
  .footer-rule--right { transform: skewY(1.5deg); }

  /* Brand lockup */
  .brand { display: flex; align-items: center; gap: 8px; }
  .brand__dot {
    width: 16px; height: 16px; border-radius: 50%;
    background: var(--sky);
  }
  .brand__name { font-size: 18px; letter-spacing: 0.3px; }
  .brand--light .brand__name { color: var(--white); }
  .brand--light .brand__dot { background: var(--white); }
  .brand--blue .brand__name { color: var(--sky); }

  /* Cards */
  .card {
    position: absolute; left: 660px;
    width: 480px; height: 274px;
    overflow: hidden;
  }
  .card--front {
    top: 150px;
    background: linear-gradient(135deg, var(--brand-blue), var(--brand-blue-deep));
    color: var(--white);
  }
  .card--back {
    top: 470px;
    background: linear-gradient(160deg, var(--white), var(--paper));
    color: var(--ink);
  }
  .card__art {
    position: absolute; right: 0; top: 30px;
    width: 200px; height: 150px;
    background: radial-gradient(circle at 60% 45%, #e9eef5 0 30%, #3a78c4 60%, var(--brand-blue) 100%);
    border-radius: 0 0 0 60px;
  }
  .card__curves { position: absolute; inset: 0; }
  .card__curves svg { width: 100%; height: 100%; display: block; }
  .card__body { position: absolute; left: 40px; top: 62px; }
  .card--back .card__body { top: 70px; }
  .card__name { font-size: 19px; letter-spacing: 1px; margin: 18px 0 4px; }
  .card--back .card__name { color: var(--sky); }
  .card__line { font-size: 11.5px; line-height: 1.55; }
  .card__line--zh { font-family: "Noto Sans TC", sans-serif; }
  .accent { color: var(--sky); }
  .card--front .accent { color: #a9d2ff; }
  .card__web {
    position: absolute; left: 170px; bottom: 30px;
    font-size: 11.5px;
  }
</style>
</head>
<body>

  <section class="letterhead" aria-label="Company letterhead">
    <div class="letterhead__header">
      <svg viewBox="0 0 540 170" preserveAspectRatio="none" aria-hidden="true">
        <path d="M0 0 H540 V170 Q300 120 0 145 Z" fill="var(--brand-blue)"/>
        <path d="M250 0 Q320 25 350 50 L330 50 Q300 25 230 0 Z" fill="var(--swoosh-grey)"/>
        <path d="M380 110 Q470 125 540 160 L540 168 Q460 135 375 122 Z" fill="var(--swoosh-grey)"/>
      </svg>
      <div class="letterhead__brand">
        <div class="brand brand--light"><span class="brand__dot"></span><span class="brand__name">Plunk Ferret Software</span></div>
      </div>
    </div>
    <div class="letterhead__footer">
      <span class="footer-rule footer-rule--left"></span>
      <div class="brand brand--blue"><span class="brand__dot"></span><span class="brand__name">Plunk Ferret Software</span></div>
      <span class="footer-rule footer-rule--right"></span>
    </div>
  </section>

  <section class="card card--front" lang="zh-Hant" aria-label="Business card, Chinese side">
    <div class="card__art" role="img" aria-label="Mascot illustration in white and blue"></div>
    <div class="card__curves">
      <svg viewBox="0 0 480 274" preserveAspectRatio="none" aria-hidden="true">
        <path d="M330 230 Q420 240 480 274 L470 274 Q410 248 330 238 Z" fill="var(--swoosh-grey)"/>
      </svg>
    </div>
    <div class="card__body">
      <div class="brand brand--light"><span class="brand__dot"></span><span class="brand__name">Plunk Ferret Software</span></div>
      <p class="card__name">Full Name</p>
      <p class="card__line">Occupation | name@plunkferret.example</p>
      <p class="card__line">P+886-2-51384470 | M+886-2-51384470 | F+886-2-51384492</p>
      <p class="card__line card__line--zh">台灣台北市大里區國源路91巷63號7樓之2</p>
    </div>
    <p class="card__web">www.plunkferret.example</p>
  </section>

  <section class="card card--back" aria-label="Business card, English side">
    <div class="card__curves">
      <svg viewBox="0 0 480 274" preserveAspectRatio="none" aria-hidden="true">
        <path d="M0 0 Q240 40 480 22 L480 30 Q240 50 0 8 Z" fill="var(--brand-navy)"/>
        <path d="M0 236 Q80 238 160 250 L160 256 Q80 244 0 242 Z" fill="var(--brand-navy)"/>
        <path d="M340 250 Q420 254 480 274 L470 274 Q410 262 340 256 Z" fill="var(--brand-navy)"/>
      </svg>
    </div>
    <div class="card__body">
      <div class="brand brand--blue"><span class="brand__dot"></span><span class="brand__name">Plunk Ferret Software</span></div>
      <p class="card__name">Full Name</p>
      <p class="card__line"><span class="accent">Occupation</span> | name@plunkferret.example</p>
      <p class="card__line"><span class="accent">P</span>+886-2-51384470 | <span class="accent">M</span>+886-2-51384470 | <span class="accent">F</span>+886-2-51384492</p>
      <p class="card__line">7F-2, NO. 63, Lane 91, Guoyuan Road, Dali District, Taipei Taiwan</p>
    </div>
    <p class="card__web">www.plunkferret.example</p>
  </section>

</body>
</html>
```